Anzeigengestaltung für KFZ-Werkstatt
Zielgruppe
Wir sind eine KFZ-Werkstatt mit vielumfänglichen Dienstleistungen. Unsere Zielgruppe beschränkt sich auf einen Umkreis von ca. 10km. Wir bieten alles rund ums KFZ: Service, Inspektion, Reparaturen aller Art, TÜV, Rad/Reifen/Felgen, Spurvermessung, Unfallinstandsetzung.
Aufgabenstellung
wir nutzen den Hashtag '#wagenhofmoosl' für Werbung im Internet sowie in den Werbeanzeigen. Wir verwenden diesen 'Slogan' in der SChriftart 'Hashtag', diese kann überall runtergeladen werden. dieser muss in den Werbeanzeigen nicht im Vordergrund stehen, da hier die Zielgruppe eher in Richtung 40+ geht.
es muss auch Platz für die offizielle Firmierung samt Anschrift, Telefon und Internet sein (kein Fax).
was die Anzeige an sich angeht, so sollte das Motiv (gerne erst mal einfach ein Stockfoto) durch uns austauschbar sein. Sprich: wenn Reifensaison ist, wollen wir da ein eigenes Motiv reinstecken können; im Sommer wiederum ein anderes etc. Zudem verwenden wir auch Standardfotos von unserem Unternehmen, welches wir platzieren lassen wenn ein Monat mal nichts besonderes ansteht (die Werbung wird monatlich geschaltet).
Maße: 172x100mm
Hauptfarben (bedingt durch das System, an das wir angeschlossen sind):
ROT: C15 M100 Y100 K0 (oder HKS15; oder Pantone 1797)
GRAU: C0 M0 Y0 K50 (oder 50% HKS90; oder Pantone Cool Gray 7)
Aufgrund der Zielgruppe haben wir als Wunsch 'erschwinglich' angegeben. Dies soll aber nicht heißen, dass wir nicht bereit sind, für das Erstellen der Anzeige kein Geld auszugeben. Nein, damit wollen wir unterstreichen, dass es nicht irre aufgepusht sein soll mit wahnsinns-Effekten etc.

```html
<!DOCTYPE html>
<html lang="de">
<head>
<meta charset="utf-8">
<title>Anzeige Werkstatt</title>
<link rel="stylesheet" href="https://fonts.googleapis.com/css2?family=Gochi+Hand&family=Montserrat:wght@500&display=swap">
<style>
  :root {
    --page-bg: #272727;
    --brand-red: #d2232a;
    --photo-red: #a81c21;
    --brand-grey: #97989b;
    --ink: #111111;
    --white: #ffffff;
  }
  html, body {
    margin: 0;
    padding: 0;
    width: 1200px;
    height: 1200px;
    overflow: hidden;
    background: var(--page-bg);
  }
  .ad {
    position: absolute;
    left: 112px;
    top: 317px;
    width: 975px;
    height: 566px;
    font-family: "Montserrat", "Helvetica Neue", Arial, sans-serif;
  }
  .ad__hero {
    position: absolute;
    left: 0;
    top: 0;
    width: 975px;
    height: 470px;
    background: var(--brand-red);
    overflow: hidden;
  }
  .ad__photo {
    position: absolute;
    left: 512px;
    top: 0;
    width: 463px;
    height: 470px;
    background: radial-gradient(ellipse 60% 70% at 55% 65%, var(--photo-red) 0%, rgba(168,28,33,0.6) 55%, rgba(210,35,42,0) 100%);
  }
  .ad__hashtag {
    position: absolute;
    left: 50px;
    top: 28px;
    margin: 0;
    font-family: "Gochi Hand", cursive;
    font-weight: 400;
    font-size: 112px;
    line-height: 1;
    color: var(--white);
    letter-spacing: -1px;
  }
  .ad__services {
    position: absolute;
    left: 98px;
    top: 179px;
    margin: 0;
    padding: 0;
    list-style: none;
  }
  .ad__service {
    position: relative;
    padding-left: 33px;
    height: 36px;
    line-height: 36px;
    font-size: 25px;
    letter-spacing: 0.5px;
    color: var(--white);
    text-transform: uppercase;
  }
  .ad__service::before {
    content: "";
    position: absolute;
    left: 0;
    top: 14px;
    width: 7px;
    height: 7px;
    border-radius: 50%;
    background: var(--white);
  }
  .ad__contact {
    position: absolute;
    left: 0;
    top: 470px;
    width: 975px;
    height: 96px;
    background: var(--brand-grey);
    color: var(--ink);
    font-size: 24px;
  }
  .contact__item {
    position: absolute;
    top: 0;
    height: 96px;
    display: flex;
    align-items: center;
    white-space: nowrap;
  }
  .contact__address { left: 40px; letter-spacing: 0.5px; }
  .contact__phone { left: 368px; }
  .contact__mail { left: 607px; }
  .contact__icon { margin-right: 9px; display: block; }
</style>
</head>
<body>
  <div class="ad">
    <section class="ad__hero">
      <div class="ad__photo" role="img" aria-label="Austauschbares Motiv: Kfz-Mechaniker im Overall mit Schraubenschlüssel, rot eingefärbt"></div>
      <h1 class="ad__hashtag">#wagenhofmoosl</h1>
      <ul class="ad__services">
        <li class="ad__service">Service</li>
        <li class="ad__service">Inspektion</li>
        <li class="ad__service">Reparaturen aller Art</li>
        <li class="ad__service">TÜV</li>
        <li class="ad__service">Rad/Reifen/Felgen</li>
        <li class="ad__service">Spurvermessung</li>
        <li class="ad__service">Unfallinstandsetzung</li>
      </ul>
    </section>
    <footer class="ad__contact">
      <div class="contact__item contact__address">TALWEG 12</div>
      <div class="contact__item contact__phone">
        <svg class="contact__icon" width="44" height="44" viewBox="0 0 44 44" aria-hidden="true">
          <circle cx="22" cy="22" r="22" fill="#111"/>
          <path d="M28 11 l4 4 -3 3 c-2-1-3-1-4 0 l-6 8 c-1 1-1 2 0 4 l-3 3 -4-4 c0-6 10-18 16-18z" fill="none" stroke="#97989b" stroke-width="2" stroke-linejoin="round"/>
        </svg>
        <span>01234-5678</span>
      </div>
      <div class="contact__item contact__mail">
        <svg class="contact__icon" width="38" height="30" viewBox="0 0 38 30" aria-hidden="true">
          <rect x="0" y="0" width="38" height="30" rx="2" fill="#111"/>
          <path d="M1 2 L19 17 L37 2" fill="none" stroke="#97989b" stroke-width="2.2"/>
          <path d="M1 28 L14 14 M37 28 L24 14" fill="none" stroke="#97989b" stroke-width="2"/>
        </svg>
        <span>info@wagenhof-moosl.de</span>
      </div>
    </footer>
  </div>
</body>
</html>
```